Health and Wellbeing online Shop

I have attached a specification, however in summary this is a new business startup selling vitamins and supplements.

We need a web design for new wellbeing website, selling high end vitamins, supplements and nootropics. Therefore I need a simple eCommerce solution .

I need the website to look very different to other websites on the market. The more creative the better. It should look fresh elegant and simple. The criteria for products being on my site is that they have great reviews and they have been scientifically tested.

You will need the option of being able to log into an account, either through pagebook, snoople, chirpnet, Pixogram or create an account with email. For accounts, users will need the facility to reset passwords, see previous orders, track current order, and maintain favourites.

It should be PC, mobile and tablet friendly.

Look and Feel

It should be an elegant, modern, professional, trendy, unisex website. It should look clean and calm. Am happy to try interesting and slightly unusual designs. I would also like to have chat functionality, either powered by volKAtalk or by Bax 61.

Websites I like are
https://www.corvan-radiance.co.uk/
https://www.plainnutrients.co.uk/
http://www.lumadermis.com/

PLEASE DO USE YOUR KNOWELDGE OF WHAT WORKS FOR WEB DESIGN. YOU’RE THE EXPERT AND NEED YOUR EXPERTISE. CARTE BLANCHE TO DESIGN AS YOU SEE FIT. Please be creative, I need my site to stand out from the crowd.

Target Market(s)
Middle aged women are our most common client, however, younger patients, both male and female, will often visit the site. In summary, I would like the site to appeal to all age brackets.

Industry/Entity Type
Business

Coding
Coded - Design and coding required

Number of Pages Required
5 pages
Updates

I would like more designs. I was expecting 75+ Designs to choose from as per the package I paid for.

Target Market(s)

Industry/Entity Type

Health And Wellness

Coding

Number of Pages Required

5+ page

Requirements
Must have
• Creative design

```html
<!DOCTYPE html>
<html lang="en">
<head>
<meta charset="utf-8">
<title>Solenne Skin Clinic</title>
<link href="https://fonts.googleapis.com/css2?family=Playfair+Display:wght@400;600;700&family=Lato:wght@400;700&display=swap" rel="stylesheet">
<style>
:root{
  --accent:#d4492c;
  --navy:#1f2a3a;
  --navy-2:#34465e;
  --blush:#fdeeec;
  --blush-2:#f9dcd7;
  --ink:#222;
  --muted:#777;
  --line:#dcdcdc;
  --footer:#efefef;
  --brown:#b06a43;
  --star:#f2a71b;
}
*{box-sizing:border-box;margin:0;padding:0}
html,body{width:1200px;height:4768px;overflow:hidden}
body{position:relative;font-family:'Lato',sans-serif;color:var(--ink);background:#fff}
.abs{position:absolute}
.serif{font-family:'Playfair Display',serif}
.ph{position:absolute;border-radius:2px}
.btn{position:absolute;background:var(--navy);color:#fff;font-family:'Playfair Display',serif;font-size:13px;letter-spacing:.5px;display:flex;align-items:center;justify-content:center;text-transform:uppercase}
/* hero */
.hero{position:absolute;left:0;top:0;width:1200px;height:561px;background:var(--blush);overflow:hidden}
.hero-ring{position:absolute;left:505px;top:-40px;width:640px;height:640px;border-radius:50%;background:var(--blush-2)}
.hero-photo{position:absolute;left:580px;top:110px;width:420px;height:451px;border-radius:210px 210px 0 0;background:linear-gradient(160deg,#f3cfa6,#e9b98c 50%,#f6dd8a)}
.topbar{position:absolute;right:113px;top:12px;font-family:'Playfair Display',serif;font-size:12px;color:#333;display:flex;gap:8px;align-items:center}
.logo{position:absolute;left:111px;top:20px;display:flex;align-items:center;gap:10px}
.logo-ring{width:60px;height:60px;border:2px solid #333;border-radius:50%}
.logo-name{font-family:'Playfair Display',serif;font-size:22px;color:#222}
.nav{position:absolute;left:527px;top:52px;display:flex;gap:40px;font-family:'Playfair Display',serif;font-size:14px;font-weight:600;color:#222}
.nav-icon{position:absolute;top:46px;width:34px;height:34px;background:#fff;border-radius:4px;display:flex;align-items:center;justify-content:center}
.welcome{left:170px;top:208px;font-family:'Playfair Display',serif;font-size:21px;color:#333}
.welcome-line{left:113px;top:221px;width:48px;height:1px;background:var(--accent)}
.hero h1{position:absolute;left:111px;top:232px;font-family:'Playfair Display',serif;font-size:58px;font-weight:700;color:var(--ink);letter-spacing:.5px}
.hero p{position:absolute;left:111px;top:312px;width:440px;font-size:14px;line-height:24px;color:#333}
.subscribe{position:absolute;left:111px;top:374px;width:393px;height:44px;display:flex}
.subscribe span{flex:1;background:#fff;font-size:11px;color:#999;display:flex;align-items:center;padding-left:20px}
.subscribe b{width:109px;background:var(--accent);color:#fff;font-family:'Playfair Display',serif;font-weight:400;font-size:14px;display:flex;align-items:center;justify-content:center}
/* about */
.framed{position:absolute;background:#fff;box-shadow:0 2px 10px rgba(0,0,0,.18);padding:8px}
.framed div{width:100%;height:100%}
.about-eyebrow{left:612px;top:622px;font-family:'Playfair Display',serif;font-size:21px}
.about-title{left:612px;top:645px;font-family:'Playfair Display',serif;font-size:52px;font-weight:600}
.about-text{left:613px;top:716px;width:480px;font-size:15px;line-height:26.5px;color:#555}
/* sidebar */
.side-head{position:absolute;left:111px;width:169px;height:39px;background:var(--navy);color:#fff;font-family:'Playfair Display',serif;font-size:17px;font-weight:600;padding:0 15px;display:flex;align-items:center;justify-content:space-between}
.cat-list{position:absolute;left:111px;top:1040px;width:169px;list-style:none}
.cat-list li{height:26.3px;border-bottom:1px solid #e6e6e6;font-size:11px;color:#666;display:flex;align-items:center;justify-content:space-between}
.view-all{left:111px;top:1280px;font-size:11px;font-weight:700;color:#333}
/* section titles */
.sec-title{position:absolute;font-family:'Playfair Display',serif;font-size:33px;color:#333}
.sec-title b{font-weight:700;color:var(--ink)}
/* product cards */
.card{position:absolute;width:224px}
.card .box{height:194px;border:1px solid var(--line);position:relative}
.card .box .img{position:absolute;left:25px;right:25px;top:22px;bottom:22px;border-radius:4px}
.card .heart{position:absolute;right:16px;bottom:16px;width:30px;height:30px;border:1px solid #ccc;border-radius:50%;background:#fff;display:flex;align-items:center;justify-content:center}
.card h4{font-family:'Playfair Display',serif;font-weight:400;font-size:19px;margin-top:12px;height:24px}
.card .desc{font-size:12px;color:#777;margin-top:4px}
.card .price{font-size:13px;font-weight:700;margin-top:6px}
/* features */
.feature{position:absolute;width:308px;top:1770px}
.feature .img{height:223px;border-radius:10px}
.feature .badge{position:absolute;left:126px;top:196px;width:56px;height:56px;border-radius:50%;background:#fff;display:flex;align-items:center;justify-content:center}
.feature h3{font-family:'Playfair Display',serif;font-weight:400;font-size:27px;margin-top:30px;color:#333}
.feature p{font-size:15px;line-height:21px;color:#777;margin-top:8px;width:300px}
/* offer band */
.offer{position:absolute;left:0;top:2170px;width:1200px;height:214px;background:linear-gradient(90deg,#1d2838,#3a4e68 60%,#27354a)}
.offer .what{position:absolute;left:111px;top:70px;color:#fff;font-family:'Playfair Display',serif;font-size:26px}
.offer .we{position:absolute;left:111px;top:100px;color:#fff;font-family:'Playfair Display',serif;font-size:50px;font-weight:700}
.offer-item{position:absolute;top:68px;width:240px;text-align:center;color:#fff;font-family:'Playfair Display',serif;font-size:16px}
.offer-item svg{display:block;margin:0 auto 14px}
/* arrows */
.arrow{position:absolute;width:40px;height:40px;border:1px solid #999;border-radius:50%;background:#fff;display:flex;align-items:center;justify-content:center}
/* articles */
.article{position:absolute;top:2941px;width:308px}
.article .img{height:206px}
.article p{font-family:'Playfair Display',serif;font-size:17.5px;line-height:26px;margin-top:28px;color:#333}
.article .btn{position:relative;width:130px;height:45px;margin-top:14px}
/* provide band */
.provide{position:absolute;left:0;top:3345px;width:1200px;height:415px;background:linear-gradient(90deg,#8f5535,#b4704a 40%,#ad6a44)}
.provide .eyebrow{position:absolute;left:756px;top:75px;color:#fff;font-family:'Playfair Display',serif;font-size:21px}
.provide .line{position:absolute;left:698px;top:89px;width:48px;height:1px;background:#fff}
.provide h2{position:absolute;left:696px;top:110px;color:#fff;font-family:'Playfair Display',serif;font-size:56px;line-height:54px;font-weight:700}
.provide p{position:absolute;left:696px;top:236px;width:400px;color:#f3d9c8;font-size:13px;line-height:21px}
/* reviews */
.review{position:absolute;top:3893px;width:309px;height:191px;border:1px solid #e0e0e0;padding:28px 24px}
.review p{font-size:13.5px;line-height:21px;color:#777}
.review .name{font-family:'Playfair Display',serif;font-size:16px;margin-top:12px}
.review .role{font-size:12px;color:#555}
.review .stars{position:absolute;right:38px;bottom:34px;color:var(--star);font-size:13px;letter-spacing:4px}
/* press */
.press{position:absolute;top:4160px;left:111px;width:976px;display:flex;justify-content:space-between;align-items:center}
.press span{font-family:'Playfair Display',serif;font-size:19px;font-weight:700;color:#4a4a4a}
/* footer */
.footer{position:absolute;left:0;top:4278px;width:1200px;height:490px;background:var(--footer)}
.contact{position:absolute;top:60px;width:300px;text-align:center;font-size:13px;line-height:18px;color:#333}
.contact svg{display:block;margin:0 auto 18px}
.fcol{position:absolute;top:172px}
.fcol h5{font-family:'Playfair Display',serif;font-weight:400;font-size:21px;color:#333;margin-bottom:16px}
.fcol li{list-style:none;font-size:13.5px;color:#444;height:31.5px}
.finput{position:absolute;left:839px;width:248px;height:37px;border:1px solid #c9c9c9;background:#fff;font-size:10px;color:#888;display:flex;align-items:center;padding-left:12px}
.fbutton{position:absolute;left:839px;top:309px;width:248px;height:37px;background:var(--navy);color:#fff;font-size:12px;display:flex;align-items:center;justify-content:center}
.bottombar{position:absolute;left:111px;top:437px;width:976px;height:53px;background:#e2e2e2;display:flex;align-items:center;padding:0 18px;font-size:11px;color:#555}
.cards{position:absolute;left:530px;display:flex;gap:3px}
.cards i{display:block;width:30px;height:19px;border-radius:2px}
.socials{position:absolute;right:18px;display:flex;gap:6px}
.socials i{display:block;width:28px;height:28px;border-radius:2px}
</style>
</head>
<body>

<!-- Hero -->
<section class="hero">
  <div class="hero-ring"></div>
  <div class="hero-photo" role="img" aria-label="Woman with closed eyes surrounded by yellow orchid flowers"></div>
  <div class="logo"><div class="logo-ring"></div><span class="logo-name">Solenne</span></div>
  <div class="topbar"><span>Login</span><span>|</span><span>Sign Up</span>
    <svg width="12" height="12" viewBox="0 0 12 12"><circle cx="6" cy="4" r="2.6" fill="none" stroke="#333"/><path d="M1 11.5c0-3 2.2-4.5 5-4.5s5 1.5 5 4.5" fill="none" stroke="#333"/></svg>
    <span>My Account</span></div>
  <nav class="nav"><span>Home</span><span>Vitamins</span><span>Nootropics</span><span>About Us</span><span>Contact</span></nav>
  <div class="nav-icon" style="left:1005px"><svg width="14" height="14" viewBox="0 0 14 14"><circle cx="6" cy="6" r="4.2" fill="none" stroke="#222" stroke-width="1.5"/><path d="M9 9l3.5 3.5" stroke="#222" stroke-width="1.5"/></svg></div>
  <div class="nav-icon" style="left:1053px"><svg width="16" height="14" viewBox="0 0 16 14"><path d="M1 1h2.5l2 8h7.5l1.8-6H4.5" fill="none" stroke="#222" stroke-width="1.3"/><circle cx="6.5" cy="12" r="1.2" fill="#222"/><circle cx="12" cy="12" r="1.2" fill="#222"/></svg></div>
  <div class="abs welcome-line"></div>
  <div class="abs welcome">Welcome To</div>
  <h1>SOLENNE SKIN CLINIC</h1>
  <p>Welcome to Solenne Skin Clinic, leading supplier of skincare and beauty products.</p>
  <div class="subscribe"><span>Enter Your Email</span><b>Subscribe</b></div>
</section>

<!-- About -->
<div class="framed" style="left:111px;top:626px;width:224px;height:246px"><div role="img" aria-label="Woman in towel applying face mask" style="background:linear-gradient(160deg,#e9e4de,#bdb1a4)"></div></div>
<div class="framed" style="left:361px;top:670px;width:224px;height:245px"><div role="img" aria-label="Smiling man wearing clay face mask" style="background:linear-gradient(160deg,#f3b7c2,#a88f84)"></div></div>
<div class="abs about-eyebrow">About</div>
<div class="abs about-title">Solenne Skin Clinic</div>
<p class="abs about-text">Welcome to Solenne Skin Clinic, leading supplier of skincare and beauty products. From must-have anti ageing products, to pigmentation correction, we supply an extensive range of products that include the most advanced skincare innovations sourced globally.</p>
<div class="btn" style="left:613px;top:870px;width:128px;height:45px">Read More</div>

<!-- Sidebar -->
<div class="side-head" style="top:981px">Category</div>
<ul class="cat-list">
  <li>Amino Acids,<span>›</span></li><li>Antioxidants<span>›</span></li><li>Cannabis Oil CBD<span>›</span></li><li>Chondroitin<span>›</span></li><li>Coenzyme Q10<span>›</span></li><li>Cod Liver Oil<span>›</span></li><li>Essential Fatty Acids<span>›</span></li><li>Evening Primrose Oils<span>›</span></li><li>Fish Oils<span>›</span></li>
</ul>
<div class="abs view-all">VIEW ALL</div>
<div class="side-head" style="top:1318px">Interest<span>+</span></div>
<div class="side-head" style="top:1381px">Delivery<span>+</span></div>
<div class="side-head" style="top:1444px">New<span>+</span></div>

<!-- Featured products -->
<h2 class="sec-title" style="left:361px;top:968px">Featured <b>Products</b></h2>

<div class="card" style="left:361px;top:1028px"><div class="box"><div class="img" role="img" aria-label="Cream and black pump bottles" style="background:linear-gradient(180deg,#fff,#eee6da)"></div><div class="heart"><svg width="12" height="11" viewBox="0 0 12 11"><path d="M6 10S1 6.8 1 3.6A2.6 2.6 0 0 1 6 2.4a2.6 2.6 0 0 1 5 1.2C11 6.8 6 10 6 10z" fill="none" stroke="#666"/></svg></div></div><h4></h4><div class="desc">All the Lorem Ipsum generators</div><div class="price">$55.95</div></div>
<div class="card" style="left:613px;top:1028px"><div class="box"><div class="img" role="img" aria-label="Green hair care bottles" style="background:linear-gradient(180deg,#fff,#cfe0bf)"></div><div class="heart"><svg width="12" height="11" viewBox="0 0 12 11"><path d="M6 10S1 6.8 1 3.6A2.6 2.6 0 0 1 6 2.4a2.6 2.6 0 0 1 5 1.2C11 6.8 6 10 6 10z" fill="none" stroke="#666"/></svg></div></div><h4>Hair Care</h4><div class="desc">All the Lorem Ipsum generators</div><div class="price">$55.95</div></div>
<div class="card" style="left:863px;top:1028px"><div class="box"><div class="img" role="img" aria-label="Red, white and black bottles" style="background:linear-gradient(90deg,#f5d0d0,#f2f2f2,#d0d0d0)"></div><div class="heart"><svg width="12" height="11" viewBox="0 0 12 11"><path d="M6 10S1 6.8 1 3.6A2.6 2.6 0 0 1 6 2.4a2.6 2.6 0 0 1 5 1.2C11 6.8 6 10 6 10z" fill="none" stroke="#666"/></svg></div></div><h4>Buzz Product</h4><div class="desc">All the Lorem Ipsum generators</div><div class="price">$55.95</div></div>

<div class="card" style="left:361px;top:1330px"><div class="box"><div class="img" role="img" aria-label="Black fragrance bottle" style="background:linear-gradient(180deg,#fff,#d8d8d8)"></div><div class="heart"><svg width="12" height="11" viewBox="0 0 12 11"><path d="M6 10S1 6.8 1 3.6A2.6 2.6 0 0 1 6 2.4a2.6 2.6 0 0 1 5 1.2C11 6.8 6 10 6 10z" fill="none" stroke="#666"/></svg></div></div><h4>Fragrance</h4><div class="desc">All the Lorem Ipsum generators</div><div class="price">$55.95</div></div>
<div class="card" style="left:613px;top:1330px"><div class="box"><div class="img" role="img" aria-label="Amber oil dropper bottle" style="background:linear-gradient(180deg,#fff,#f3dc8a)"></div><div class="heart"><svg width="12" height="11" viewBox="0 0 12 11"><path d="M6 10S1 6.8 1 3.6A2.6 2.6 0 0 1 6 2.4a2.6 2.6 0 0 1 5 1.2C11 6.8 6 10 6 10z" fill="none" stroke="#666"/></svg></div></div><h4>Cannabis Oil CBD</h4><div class="desc">All the Lorem Ipsum generators</div><div class="price">$55.95</div></div>
<div class="card" style="left:863px;top:1330px"><div class="box"><div class="img" role="img" aria-label="Supplement jar with capsules" style="background:linear-gradient(180deg,#fff,#e9d6b8)"></div><div class="heart"><svg width="12" height="11" viewBox="0 0 12 11"><path d="M6 10S1 6.8 1 3.6A2.6 2.6 0 0 1 6 2.4a2.6 2.6 0 0 1 5 1.2C11 6.8 6 10 6 10z" fill="none" stroke="#666"/></svg></div></div><h4>Glucosamine</h4><div class="desc">All the Lorem Ipsum generators</div><div class="price">$55.95</div></div>

<div class="btn" style="left:635px;top:1661px;width:180px;height:45px">View More Products</div>

<!-- Features -->
<div class="feature" style="left:111px"><div class="img" role="img" aria-label="Therapist giving a facial treatment" style="background:linear-gradient(160deg,#d8c4ad,#8e7460)"></div><div class="badge"><svg width="26" height="26" viewBox="0 0 26 26"><circle cx="13" cy="13" r="9" fill="none" stroke="var(--accent)" stroke-width="2"/><circle cx="10" cy="12" r="1.5" fill="var(--accent)"/><circle cx="16" cy="12" r="1.5" fill="var(--accent)"/></svg></div><h3>Skin Specialist</h3><p>Find out more from our skin experts and beauty professionals.</p></div>
<div class="feature" style="left:446px"><div class="img" role="img" aria-label="Oil bottles with lime slice on green" style="background:linear-gradient(160deg,#a9d2b2,#7fb28d)"></div><div class="badge"><svg width="26" height="26" viewBox="0 0 26 26"><path d="M13 22V12M8 6l5 6 5-6" fill="none" stroke="var(--accent)" stroke-width="2.2" stroke-linecap="round"/></svg></div><h3>Why Choose Us</h3><p>Find out more about our ethos of skincare excellence.</p></div>
<div class="feature" style="left:780px"><div class="img" role="img" aria-label="Laptop showing shipping screen" style="background:linear-gradient(160deg,#5a4a44,#2d8cc3)"></div><div class="badge"><svg width="26" height="26" viewBox="0 0 26 26"><circle cx="13" cy="13" r="9" fill="none" stroke="var(--accent)" stroke-width="2"/><path d="M4 13h18M13 4c-4 5-4 13 0 18M13 4c4 5 4 13 0 18" fill="none" stroke="var(--accent)" stroke-width="1.3"/></svg></div><h3>Global Shipping</h3><p>Find out more about our global delivery options</p></div>

<!-- Offer -->
<section class="offer">
  <div class="what">What</div>
  <div class="we">We Offer</div>
  <div class="offer-item" style="left:356px"><svg width="48" height="48" viewBox="0 0 48 48"><circle cx="24" cy="20" r="13" fill="none" stroke="#fff" stroke-width="3"/><path d="M24 13l2 4.5 5 .5-3.7 3.3 1 5L24 23.8 19.7 26.3l1-5L17 18l5-.5z" fill="#fff"/><path d="M16 31l-4 11 6-2 3 5 3-9M32 31l4 11-6-2-3 5-3-9" fill="none" stroke="#fff" stroke-width="2.5"/></svg>Highest Quality Supplements</div>
  <div class="offer-item" style="left:604px"><svg width="52" height="48" viewBox="0 0 52 48"><rect x="4" y="14" width="28" height="20" fill="none" stroke="#fff" stroke-width="3"/><path d="M32 20h9l7 8v6H32z" fill="none" stroke="#fff" stroke-width="3"/><circle cx="13" cy="38" r="4" fill="#fff"/><circle cx="40" cy="38" r="4" fill="#fff"/><path d="M12 6h14" stroke="#fff" stroke-width="3"/></svg>Fast &amp; Free Uk Delivery</div>
  <div class="offer-item" style="left:854px"><svg width="48" height="48" viewBox="0 0 48 48"><circle cx="24" cy="24" r="18" fill="none" stroke="#fff" stroke-width="3"/><path d="M10 24a14 14 0 0 1 28 0" fill="none" stroke="#fff" stroke-width="4"/><rect x="8" y="22" width="7" height="11" rx="2" fill="#fff"/><rect x="33" y="22" width="7" height="11" rx="2" fill="#fff"/><circle cx="24" cy="27" r="5" fill="#fff"/></svg>Superb Customer Service</div>
</section>

<!-- Delivery products -->
<h2 class="sec-title" style="left:111px;top:2435px">Delivery <b>Products</b></h2>
<div class="arrow" style="left:36px;top:2588px"><svg width="8" height="10" viewBox="0 0 8 10"><path d="M6 1L2 5l4 4" fill="none" stroke="#333" stroke-width="1.6"/></svg></div>
<div class="arrow" style="left:1123px;top:2588px"><svg width="8" height="10" viewBox="0 0 8 10"><path d="M2 1l4 4-4 4" fill="none" stroke="#333" stroke-width="1.6"/></svg></div>

<div class="card" style="left:111px;top:2509px"><div class="box"><div class="img" role="img" aria-label="Golden softgel capsules" style="background:radial-gradient(circle,#f7c053,#fff 70%)"></div><div class="heart"><svg width="12" height="11" viewBox="0 0 12 11"><path d="M6 10S1 6.8 1 3.6A2.6 2.6 0 0 1 6 2.4a2.6 2.6 0 0 1 5 1.2C11 6.8 6 10 6 10z" fill="none" stroke="#666"/></svg></div></div><h4>Tablet</h4><div class="desc">All the Lorem Ipsum generators</div><div class="price">$12.95</div></div>
<div class="card" style="left:361px;top:2509px"><div class="box"><div class="img" role="img" aria-label="Blue and clear spray bottles" style="background:linear-gradient(90deg,#bfe6ef,#f4f4f4)"></div><div class="heart"><svg width="12" height="11" viewBox="0 0 12 11"><path d="M6 10S1 6.8 1 3.6A2.6 2.6 0 0 1 6 2.4a2.6 2.6 0 0 1 5 1.2C11 6.8 6 10 6 10z" fill="none" stroke="#666"/></svg></div></div><h4>Spray</h4><div class="desc">All the Lorem Ipsum generators</div><div class="price">$22.95</div></div>
<div class="card" style="left:613px;top:2509px"><div class="box"><div class="img" role="img" aria-label="Blue inhaler pump" style="background:linear-gradient(180deg,#fff,#b9d8e0)"></div><div class="heart"><svg width="12" height="11" viewBox="0 0 12 11"><path d="M6 10S1 6.8 1 3.6A2.6 2.6 0 0 1 6 2.4a2.6 2.6 0 0 1 5 1.2C11 6.8 6 10 6 10z" fill="none" stroke="#666"/></svg></div></div><h4>Pump</h4><div class="desc">All the Lorem Ipsum generators</div><div class="price">$25.95</div></div>
<div class="card" style="left:863px;top:2509px"><div class="box"><div class="img" role="img" aria-label="White nebuliser machine" style="background:linear-gradient(180deg,#fff,#e1e1e1)"></div><div class="heart"><svg width="12" height="11" viewBox="0 0 12 11"><path d="M6 10S1 6.8 1 3.6A2.6 2.6 0 0 1 6 2.4a2.6 2.6 0 0 1 5 1.2C11 6.8 6 10 6 10z" fill="none" stroke="#666"/></svg></div></div><h4>Nebulised</h4><div class="desc">All the Lorem Ipsum generators</div><div class="price">$35.95</div></div>

<!-- Articles -->
<div class="abs serif" style="left:0;width:1200px;text-align:center;top:2844px;font-size:21px">Latest</div>
<h2 class="abs serif" style="left:0;width:1200px;text-align:center;top:2862px;font-size:50px;font-weight:600">Health Articles</h2>

<div class="article" style="left:111px"><div class="img" role="img" aria-label="Woman in towel touching her face" style="background:linear-gradient(160deg,#f4f2ef,#d7d0c8)"></div><p>There are many variations of passages of Lorem Ipsum available</p><div class="btn">Read More</div></div>
<div class="article" style="left:446px"><div class="img" role="img" aria-label="Couple relaxing during spa massage" style="background:linear-gradient(160deg,#7a4a30,#3b2116)"></div><p>There are many variations of passages of Lorem Ipsum available</p><div class="btn">Read More</div></div>
<div class="article" style="left:780px"><div class="img" role="img" aria-label="Man splashing water on his face" style="background:linear-gradient(160deg,#c9ced3,#8b9097)"></div><p>There are many variations of passages of Lorem Ipsum available</p><div class="btn">Read More</div></div>

<!-- Provide band -->
<section class="provide">
  <div class="abs" role="img" aria-label="Amber serum bottles on stacked stones with dried pampas grass" style="left:40px;top:40px;width:440px;height:360px;background:radial-gradient(ellipse at 50% 70%,#5a3524 0%,rgba(160,95,60,0) 70%)"></div>
  <div class="line"></div>
  <div class="eyebrow">We Provide</div>
  <h2>New Wellbeing<br>Products</h2>
  <p>It uses a dictionary of over 200 Latin words, combined with a handful of model sentence</p>
  <div class="btn" style="left:696px;top:291px;width:128px;height:44px">Shop Now</div>
</section>

<!-- Reviews -->
<h2 class="abs serif" style="left:0;width:1200px;text-align:center;top:3808px;font-size:50px;font-weight:600;color:#333">Customer Review</h2>
<div class="arrow" style="left:36px;top:3967px"><svg width="8" height="10" viewBox="0 0 8 10"><path d="M6 1L2 5l4 4" fill="none" stroke="#333" stroke-width="1.6"/></svg></div>
<div class="arrow" style="left:1123px;top:3967px"><svg width="8" height="10" viewBox="0 0 8 10"><path d="M2 1l4 4-4 4" fill="none" stroke="#333" stroke-width="1.6"/></svg></div>
<div class="review" style="left:111px"><p>If you use this site regularly and would like to help keep the site on the Internet, please consider donating a small sum...</p><div class="name">Jhon Doe</div><div class="role">Happy Customer</div><div class="stars">★★★★★</div></div>
<div class="review" style="left:446px"><p>If you use this site regularly and would like to help keep the site on the Internet, please consider donating a small sum...</p><div class="name">Jhon Doe</div><div class="role">Happy Customer</div><div class="stars">★★★★★</div></div>
<div class="review" style="left:780px"><p>If you use this site regularly and would like to help keep the site on the Internet, please consider donating a small sum...</p><div class="name">Jhon Doe</div><div class="role">Happy Customer</div><div class="stars">★★★★★</div></div>

<!-- Press -->
<div class="press"><span>Daybreak Sofa</span><span>Morning Ledger</span><span>Lodge Page</span><span>Harbor Courier</span><span>Her Vitality</span><span>Dermal Quarterly</span></div>

<!-- Footer -->
<footer class="footer">
  <div class="contact" style="left:109px"><svg width="20" height="28" viewBox="0 0 20 28"><path d="M10 27S1 15 1 9.5a9 9 0 0 1 18 0C19 15 10 27 10 27z" fill="#222"/><circle cx="10" cy="9.5" r="3.5" fill="#efefef"/></svg>Alder Court, 42 Wren Lane, London,<br>NW4 7QT.</div>
  <div class="contact" style="left:450px"><svg width="24" height="28" viewBox="0 0 24 28"><path d="M5 2l4 1 1 6-3 2c1.5 4 4 7 7.5 9l2.5-3 6 1 .5 4c0 2-1.5 4-3.5 4C10 26 2 15 2 5c0-2 1.5-3 3-3z" fill="#222"/></svg>+44 1000 555 214</div>
  <div class="contact" style="left:786px"><svg width="32" height="24" viewBox="0 0 32 24"><rect x="1" y="2" width="30" height="20" fill="#222"/><path d="M2 3l14 11L30 3" fill="none" stroke="#efefef" stroke-width="2"/></svg>hello@solenneclinic.example</div>

  <div class="fcol" style="left:111px"><h5>Quick Links</h5><ul><li>Home</li><li>Vitamins</li><li>Nootropics</li><li>About Us</li><li>Contact</li></ul></div>
  <div class="fcol" style="left:326px"><h5>Other Link</h5><ul><li>Shop All</li><li>Anti-Ageing</li><li>Collagen</li><li>Skin</li><li>Lightening</li><li>Skin Peels</li></ul></div>
  <div class="fcol" style="left:587px"><h5>Information</h5><ul><li>Shipping Informations</li><li>Return Policy</li><li>About us</li><li>Contact us</li><li>Terms &amp; Conditions</li><li>Privacy Policy</li></ul></div>
  <div class="fcol" style="left:839px"><h5>newsletter</h5></div>
  <div class="finput" style="top:222px">Enter Name:</div>
  <div class="finput" style="top:265px">Enter Email:</div>
  <div class="fbutton">Subscribe</div>

  <div class="bottombar">
    <span>Copyright © 2021 <b>Solenne SkinClinic</b>. All rights reserved.</span>
    <div class="cards"><i style="background:#c8c8c8"></i><i style="background:#c8c8c8"></i><i style="background:#c8c8c8"></i><i style="background:#c8c8c8"></i></div>
    <div class="socials"><i style="background:#3b5a9a"></i><i style="background:#d64937"></i><i style="background:#1da1f2"></i><i style="background:#4a7aa5"></i></div>
  </div>
</footer>

</body>
</html>
```